plumweave business card

need to upgrade current business card for an online retailer of handmade arts and crafts, please visit plumweave.com.au

need to be artistic professional look

sample layout, contents, logo, are in the attached files

need for 4 people, details for other 2 people to be provided later

Industry/Entity Type

Business

```html
<!DOCTYPE html>
<html lang="en">
<head>
<meta charset="utf-8">
<title>Plumweave business card</title>
<link href="https://fonts.googleapis.com/css2?family=Lato:ital,wght@0,400;0,700;1,400&display=swap" rel="stylesheet">
<style>
  :root {
    --stage-top: #252525;
    --stage-bottom: #040404;
    --card-red: #d73d31;
    --card-white: #ffffff;
    --ink-dark: #3a322e;
    --text-light: #ffffff;
  }
  * { margin: 0; padding: 0; box-sizing: border-box; }
  html, body { width: 1200px; height: 900px; overflow: hidden; }
  body {
    position: relative;
    background: linear-gradient(180deg, var(--stage-top) 0%, #141414 55%, var(--stage-bottom) 100%);
    font-family: "Lato", Arial, sans-serif;
    color: var(--text-light);
  }
  .card {
    position: absolute;
    top: 316px;
    width: 431px;
    height: 253px;
    background: var(--card-red);
    overflow: hidden;
  }
  .card--front { left: 162px; }
  .card--back { left: 602px; }

  .brand-panel {
    position: absolute;
    left: 0; top: 0;
    width: 100%; height: 146px;
    background: var(--card-white);
    text-align: center;
    color: var(--ink-dark);
  }
  .brand-name {
    position: absolute;
    left: 0; right: 0; top: 26px;
    font-size: 62px;
    font-weight: 700;
    line-height: 1;
    letter-spacing: -1px;
  }
  .brand-tagline {
    position: absolute;
    left: 0; right: 0; top: 106px;
    font-size: 25px;
    font-weight: 400;
    line-height: 1;
    letter-spacing: 0.5px;
  }

  .contact {
    position: absolute;
    left: 26px; top: 167px;
    font-size: 13px;
    line-height: 16px;
  }
  .contact .gap { margin-top: 2px; }
  .services {
    position: absolute;
    left: 281px; top: 170px;
    font-size: 13px;
    line-height: 16px;
  }
  .services ul { list-style: none; padding-left: 3px; }
  .services li::before { content: "\2022"; margin-right: 6px; }

  .back-intro {
    position: absolute;
    left: 21px; top: 23px;
    font-size: 12.5px;
    line-height: 16px;
  }
  .product-list {
    position: absolute;
    left: 100px; top: 54px;
    font-size: 14.5px;
    font-style: italic;
    line-height: 18px;
    list-style: none;
  }
  .product-list li { position: relative; }
  .product-list li::before {
    content: "\2022";
    font-style: normal;
    position: absolute;
    left: -16px;
    font-size: 12px;
  }
  .ethos {
    position: absolute;
    left: 23px; top: 193px;
    width: 350px;
    font-size: 12.5px;
    line-height: 16px;
  }
</style>
</head>
<body>
  <section class="card card--front">
    <div class="brand-panel">
      <div class="brand-name">Plumweave</div>
      <div class="brand-tagline">weaving life by hand</div>
    </div>
    <div class="contact">
      <p>Ravi Lama</p>
      <p>Director, Plumweave Australia</p>
      <p class="gap">e ravi@plumweave.com.au</p>
      <p>p +61 400 555 017</p>
    </div>
    <div class="services">
      <p>We do hardicrafts</p>
      <ul>
        <li>design/promotion</li>
        <li>wholesale/retail</li>
        <li>import/export</li>
      </ul>
    </div>
  </section>

  <section class="card card--back">
    <p class="back-intro">Vist us for exotic hand-made arts &amp; crafts around the globe</p>
    <ul class="product-list">
      <li>cashmere fashion items from nepal</li>
      <li>thai Traditinal painting</li>
      <li>nepali/tibeten thangkas</li>
      <li>lokta/rice paper crafts</li>
      <li>allo/cotton/woollen items</li>
      <li>&nbsp;fashion/jewellery</li>
      <li>other gift/decoration items</li>
    </ul>
    <p class="ethos">We encourage eco-friendly,sustainable and traditional arts practice.</p>
  </section>
</body>
</html>
```